Domain Parking page and Listing page

1)
In need a design of a domain parking page, mainly with the same features as KOV.example as can be seen here: https://pickturnip.example/

2)
I need a design of a website with all domains listed. There's no company logo/name yet so it should be in plain font, for example "lotsbrim.example" (this is just an example), similar as:
https://kov.example/search?&terms=park&results=50&order_by=relevance

Delivery after approval in HTML/CSS. Should be responsive. Ideally use a framework like Bootstrap

Target Market(s)

Domain buyers, business owners

Industry/Entity Type

Business to business, Marketing, domains

Coding

Coded - Design and coding required

Number of Pages Required

2 page

Font styles to use
Sans Serif

Requirements
Must have
• Responsive design, worldly design.

```html
<!DOCTYPE html>
<html lang="en">
<head>
<meta charset="utf-8">
<title>Lotsbrim.example – Parking &amp; Listing Pages</title>
<link href="https://fonts.googleapis.com/css2?family=Outfit:wght@300;400;500;600;700&display=swap" rel="stylesheet">
<style>
:root{
  --board:#3baf82;
  --navy:#070c46;
  --blue-deep:#0d1f86;
  --blue:#1a5cf0;
  --blue-text:#1436b8;
  --green:#1cc47e;
  --ink:#12162e;
  --muted:#6c7082;
  --soft:#f3f6fd;
  --row:#f2f6fe;
  --line:#e3e7f0;
  --white:#ffffff;
}
*{box-sizing:border-box;margin:0;padding:0}
html,body{width:1200px;height:3084px;overflow:hidden}
body{background:var(--board);font-family:"Outfit",sans-serif;color:var(--ink);position:relative}
.board-title{position:absolute;left:0;width:1200px;text-align:center;color:var(--white);font-size:39px;font-weight:500;letter-spacing:.3px}
.mock{position:absolute;background:var(--white);overflow:hidden;box-shadow:0 10px 30px rgba(0,0,0,.12)}
.hero{position:absolute;left:0;right:0;top:0;
  background:
   linear-gradient(118deg,transparent 52%,rgba(255,255,255,.05) 52%,rgba(255,255,255,.05) 64%,transparent 64%),
   linear-gradient(118deg,transparent 30%,rgba(255,255,255,.04) 30%,rgba(255,255,255,.04) 42%,transparent 42%),
   linear-gradient(180deg,var(--navy) 0,var(--navy) 60px,var(--blue-deep) 60px,#0b1a78 100%);}
.topbar{position:absolute;background:var(--white);display:flex;align-items:center;padding:0 14px}
.brand{display:flex;align-items:center;gap:10px;font-weight:600;font-size:23px;color:var(--ink)}
.brand-dot{width:28px;height:28px;border-radius:50%;background:var(--blue)}
.review{margin-left:auto;font-size:11px;color:#3a3e52;display:flex;gap:8px;align-items:center}
.review b{font-weight:600}
.review .stars{color:#f2a81d;letter-spacing:1px;font-size:12px}
.nav{margin-left:auto;display:flex;align-items:center;gap:40px;font-size:12px;color:#2b2f45}
.btn-login{border:2px solid var(--green);color:var(--green);padding:9px 20px;font-size:12px;font-weight:500;margin-left:6px}
/* parking */
.domain-head{position:absolute;left:81px;color:var(--white)}
.domain-head .label{font-size:15px;position:absolute;top:0;white-space:nowrap}
.domain-head .name{font-size:40px;font-weight:600;position:absolute;top:20px;white-space:nowrap;letter-spacing:.3px}
.domain-head .sale{font-size:21px;font-weight:300;position:absolute;top:68px;white-space:nowrap}
.seller{position:absolute;top:104px;display:flex;align-items:center;gap:10px;font-size:11px;line-height:1.4;white-space:nowrap}
.avatar{width:38px;height:38px;border-radius:50%;background:linear-gradient(135deg,#cfd8e6,#7f90ad);border:2px solid #fff}
.orb{position:absolute;width:144px;height:144px;border-radius:50%;background:linear-gradient(135deg,#2a7bff,#0d2fa8)}
.offer{position:absolute;background:var(--white);box-shadow:0 6px 24px rgba(20,30,80,.12);padding:22px 16px}
.offer h3{font-size:16px;font-weight:500;margin-bottom:16px}
.field{border:1px solid var(--line);padding:9px 10px;font-size:9px;color:var(--muted);height:48px}
.field strong{display:block;font-size:11px;color:var(--ink);font-weight:500;margin-top:3px}
.btn-blue{display:flex;align-items:center;justify-content:center;background:linear-gradient(90deg,#1a6cf5,#1448e0);color:#fff;font-weight:500;font-size:12px}
.or{display:flex;align-items:center;gap:8px;font-size:10px;color:var(--ink);margin:6px 0 4px}
.or::before,.or::after{content:"";flex:1;height:1px;background:#c9cdd8}
.btn-ghost{border:2px solid var(--green);color:var(--green);height:38px;display:flex;align-items:center;justify-content:center;font-size:12px;background:#f6fffa}
.perks{list-style:none;margin-top:20px;font-size:10px;color:#2b2f45}
.perks li{margin-bottom:13px;display:flex;gap:8px}
.perks li::before{content:"✓";color:var(--blue)}
.pay{display:flex;gap:5px;margin-top:18px}
.pay span{flex:1;height:20px;border:1px solid var(--line);border-radius:2px;background:var(--soft)}
.section-h{font-size:20px;font-weight:500}
.feature{position:absolute;width:150px;text-align:center;font-size:13px;color:var(--muted);line-height:1.3}
.feature svg{display:block;margin:0 auto 12px}
.center{position:absolute;left:0;right:0;text-align:center}
.lead{font-size:13px;color:var(--muted);line-height:1.45}
.help{position:absolute;left:0;right:0;background:var(--soft)}
.contact{position:absolute;display:flex;align-items:center;gap:18px;font-size:14px;font-weight:500}
.contact .ico{width:48px;height:48px;border-radius:50%;background:#dfe8fa;display:flex;align-items:center;justify-content:center}
.footer{position:absolute;left:0;right:0;background:var(--navy);color:#fff;font-size:10px;display:flex;align-items:center;justify-content:center;gap:14px}
/* listing */
.search-title{font-size:28px;font-weight:500;color:#fff}
.search{position:absolute;background:#fff;display:flex;align-items:center;padding:0 7px 0 18px;font-size:10px;color:var(--muted)}
.btn-green{background:var(--green);color:#fff;font-size:12px;font-weight:500;display:flex;align-items:center;justify-content:center}
.search .btn-green{margin-left:auto;width:68px;height:32px}
.meta-bar{position:absolute;font-size:12px;font-weight:500}
.select{position:absolute;border:1px solid #c7ccd8;font-size:11px;display:flex;align-items:center;justify-content:space-between;padding:0 14px;color:#2b2f45}
.sidebar{position:absolute;border:1px solid var(--line);font-size:10px;color:#2b2f45}
.f-head{height:40px;background:var(--row);color:var(--blue-text);font-size:12px;display:flex;align-items:center;justify-content:space-between;padding:0 12px}
.f-head::after{content:"";width:6px;height:6px;border-left:1.5px solid #333;border-top:1.5px solid #333;transform:rotate(45deg);margin-top:4px}
.f-body{padding:12px 12px 10px}
.check{display:flex;align-items:center;gap:10px;height:28px}
.check::before{content:"";width:15px;height:15px;border:1px solid #9ca2b3;border-radius:2px}
.row2{display:flex;align-items:center;gap:4px;font-size:10px}
.mini{height:34px;border:1px solid #c7ccd8;display:flex;align-items:center;justify-content:space-between;padding:0 8px;flex:1}
.mini::after{content:"⌄";font-size:10px;margin-top:-5px}
.range{position:relative;height:2px;background:var(--blue-text);margin:12px 0 6px}
.range::before{content:"";position:absolute;left:-2px;top:-4px;width:10px;height:10px;border-radius:50%;background:var(--blue-text)}
.ext-add{display:flex;gap:4px;margin-top:8px}
.ext-add .inp{flex:1;height:34px;border:1px solid #c7ccd8;display:flex;align-items:center;padding:0 10px}
.ext-add .plus{width:34px;height:34px;background:#e4ecfd;color:var(--blue);display:flex;align-items:center;justify-content:center;font-size:18px}
.text-inp{height:34px;border:1px solid #c7ccd8}
.listing{position:absolute;border:1px solid var(--line)}
.item{position:relative;display:flex;align-items:center;padding:0 15px 0 19px}
.item:nth-child(odd){background:var(--row)}
.item h4{font-size:13px;font-weight:500;color:var(--blue-text);margin-bottom:8px}
.specs{display:flex;gap:22px;font-size:8.5px;color:#3a3e52;line-height:1.5}
.specs span{color:#8a8ea0;display:block}
.item .act{margin-left:auto;width:95px;height:34px;font-size:12px;font-weight:500;display:flex;align-items:center;justify-content:center}
.act.view{background:var(--green);color:#fff}
.act.offer-btn{border:1.5px solid var(--green);color:var(--green);background:#fff}
.pager{position:absolute;left:0;right:0;display:flex;justify-content:center;gap:22px;font-size:10px;color:#2b2f45}
.pager .on,.pager .arr{color:var(--blue)}
</style>
</head>
<body>

<h1 class="board-title" style="top:64px">Domain Parking Page</h1>

<!-- Parking page -->
<section class="mock" style="left:137px;top:133px;width:927px;height:1028px">
  <div class="hero" style="height:329px"></div>
  <header class="topbar" style="left:82px;top:29px;width:762px;height:58px">
    <div class="brand"><span class="brand-dot"></span>Lotsbrim.example</div>
    <div class="review"><b>★ ReviewHub</b><span class="stars">★★★★★</span>4.6 out 5 based on 39837 reviews</div>
  </header>

  <div class="domain-head" style="top:138px">
    <div class="label">Domain Name</div>
    <div class="name">lumenware.example</div>
    <div class="sale">is for sale!</div>
    <div class="seller"><div class="avatar" role="img" aria-label="Seller profile picture"></div><div>Listed by<br>Private Seller</div></div>
  </div>

  <div class="orb" style="left:524px;top:123px"></div>
  <aside class="offer" style="left:583px;top:147px;width:251px;height:385px">
    <h3>Submit Your Offer</h3>
    <div class="field">My Offer in USD<strong>USD $505</strong></div>
    <div class="btn-blue" style="height:38px;margin-top:6px">Make An Offer</div>
    <div class="or">or</div>
    <div class="btn-ghost">Buy Now For $5,195</div>
    <ul class="perks">
      <li>Secure Transfer Of Your Domain</li>
      <li>Free Transaction Support</li>
      <li>Secure Payments Methods Available</li>
    </ul>
    <div class="pay" aria-label="Accepted payment methods"><span></span><span></span><span></span><span></span><span></span></div>
  </aside>

  <h2 class="section-h" style="position:absolute;left:81px;top:364px">Get Your Domain</h2>
  <div class="feature" style="left:54px;top:424px">
    <svg width="52" height="54" viewBox="0 0 52 54"><path d="M26 3 46 10v16c0 13-9 21-20 25C15 47 6 39 6 26V10z" fill="#1a5cf0"/><path d="M26 10 40 15v11c0 9-6 15-14 18-8-3-14-9-14-18V15z" fill="#5a97ff"/><path d="m18 27 6 6 11-12" stroke="#fff" stroke-width="4" fill="none" stroke-linecap="round"/></svg>
    Covered by our Buyer Protection Program
  </div>
  <div class="feature" style="left:223px;top:424px">
    <svg width="54" height="54" viewBox="0 0 54 54"><path d="M45 27A18 18 0 1 1 27 9" stroke="#1a5cf0" stroke-width="5" fill="none" stroke-linecap="round"/><path d="m27 2 8 7-8 7z" fill="#1a5cf0"/><text x="27" y="33" text-anchor="middle" font-family="Outfit,sans-serif" font-weight="700" font-size="16" fill="#1a5cf0">24</text></svg>
    Use this domain in less than 24 hours
  </div>
  <div class="feature" style="left:389px;top:424px">
    <svg width="62" height="54" viewBox="0 0 62 54"><rect x="4" y="12" width="42" height="36" rx="4" fill="#1a5cf0"/><rect x="26" y="24" width="20" height="12" rx="3" fill="#5a97ff"/><circle cx="46" cy="16" r="13" fill="#2a7bff" stroke="#fff" stroke-width="2"/><text x="46" y="21" text-anchor="middle" font-family="Outfit,sans-serif" font-weight="600" font-size="15" fill="#fff">$</text></svg>
    Safe hassle payments by our payment processor
  </div>

  <div class="center" style="top:600px"><h2 class="section-h">The simple, safe way to buy domain names</h2></div>
  <p class="center lead" style="top:643px">Lorem Ipsum has been the industry's standard dummy text ever since<br>the 1500s, when an unknown printer</p>
  <div class="btn-blue" style="position:absolute;left:354px;top:695px;width:218px;height:37px">How It Works</div>

  <div class="help" style="top:776px;height:196px">
    <h2 class="center section-h" style="top:51px">Questions?We're happy to help</h2>
    <div class="contact" style="left:295px;top:99px"><span class="ico"><svg width="20" height="20" viewBox="0 0 24 24"><path d="M6.6 10.8a15 15 0 0 0 6.6 6.6l2.2-2.2c.3-.3.7-.4 1-.2 1.1.4 2.3.6 3.6.6.6 0 1 .4 1 1V20c0 .6-.4 1-1 1A17 17 0 0 1 3 4c0-.6.4-1 1-1h3.5c.6 0 1 .4 1 1 0 1.3.2 2.5.6 3.6.1.3 0 .7-.2 1z" fill="#1a5cf0"/></svg></span>+1 - 123-456-7890</div>
    <div class="contact" style="left:522px;top:99px"><span class="ico"><svg width="20" height="16" viewBox="0 0 20 16"><rect x="1" y="1" width="18" height="14" rx="1" fill="#1a5cf0"/><path d="m1 2 9 7 9-7" stroke="#fff" stroke-width="1.6" fill="none"/></svg></span>Write Us</div>
  </div>
  <footer class="footer" style="top:972px;height:56px"><span>Terms &amp; Conditions</span><span>I</span><span>Contact Us</span><span>I</span><span>Copyright© 2023.All Right Reserved</span></footer>
</section>

<h1 class="board-title" style="top:1228px">Listning Page</h1>

<!-- Listing page -->
<section class="mock" style="left:134px;top:1304px;width:932px;height:1746px">
  <div class="hero" style="height:294px"></div>
  <header class="topbar" style="left:83px;top:30px;width:766px;height:59px">
    <div class="brand"><span class="brand-dot"></span>Lotsbrim.example</div>
    <nav class="nav"><span>Buy Domain</span><span>Sell Domain</span><span>Leran</span><span>Company</span><span class="btn-login">Log In</span></nav>
  </header>
  <div class="center" style="top:139px"><h2 class="search-title">Search Online Business For Sale</h2></div>
  <div class="search" style="left:249px;top:192px;width:434px;height:44px">park<span class="btn-green">Search</span></div>

  <div class="center" style="top:340px"><h2 class="section-h">Get Your Domain</h2></div>
  <div class="meta-bar" style="left:84px;top:398px">For Sale (5,923)</div>
  <div class="meta-bar" style="left:661px;top:398px">Sort by :</div>
  <div class="select" style="left:714px;top:386px;width:126px;height:38px">Most Relevant <span>⌄</span></div>

  <aside class="sidebar" style="left:83px;top:436px;width:225px;height:926px">
    <div class="f-head">Categories</div>
    <div class="f-body"><div class="check">Popular Domain Names</div><div class="check">3-letter Domain Names</div><div class="check">Premium Domain Names</div></div>
    <div class="f-head">Extensions</div>
    <div class="f-body"><div class="check">.com</div><div class="check">.net</div><div class="check">.org</div>
      <div class="ext-add"><div class="inp">add extension</div><div class="plus">+</div></div></div>
    <div class="f-head">Length</div>
    <div class="f-body"><div class="row2"><div class="mini">1</div>to<div class="mini">50</div></div><div class="range"></div></div>
    <div class="f-head">Price</div>
    <div class="f-body"><div class="row2"><div class="mini">0</div>to<div class="mini">10000</div></div><div class="range"></div></div>
    <div class="f-head">Name</div>
    <div class="f-body"><div class="check">No hyphen</div><div class="check">No numerals</div><div class="check">No special chars</div></div>
    <div class="f-head">Starting With</div>
    <div class="f-body"><div class="text-inp"></div></div>
    <div class="f-head">Ending With</div>
    <div class="f-body"><div class="text-inp"></div></div>
  </aside>

  <div class="listing" style="left:322px;top:436px;width:516px;height:930px">
    <div class="item" style="height:93px"><div><h4>Parksourcehub.example</h4><div class="specs"><div><span>Type</span>Domain</div><div><span>Domain Age</span>20 years</div><div><span>Industry</span>Internet</div></div></div><div class="act view">View Listing</div></div>
    <div class="item" style="height:96px"><div><h4>Parkloremipsum.example</h4><div class="specs"><div><span>Type</span>Domain</div><div><span>Domain Age</span>20 years</div><div><span>Industry</span>Internet</div></div></div><div class="act offer-btn">Make Offer</div></div>
    <div class="item" style="height:101px"><div><h4>Parkdummy.example</h4><div class="specs"><div><span>Type</span>Domain</div><div><span>Domain Age</span>20 years</div><div><span>Industry</span>Internet</div></div></div><div class="act offer-btn">Make Offer</div></div>
    <div class="item" style="height:103px"><div><h4>Parkdomainly.example</h4><div class="specs"><div><span>Type</span>Domain</div><div><span>Domain Age</span>20 years</div><div><span>Industry</span>Internet</div></div></div><div class="act offer-btn">Make Offer</div></div>
    <div class="item" style="height:102px"><div><h4>Parkdomainly.example</h4><div class="specs"><div><span>Type</span>Domain</div><div><span>Domain Age</span>20 years</div><div><span>Industry</span>Internet</div></div></div><div class="act offer-btn">Make Offer</div></div>
    <div class="item" style="height:113px"><div><h4>Parkdomainly.example</h4><div class="specs"><div><span>Type</span>Domain</div><div><span>Domain Age</span>20 years</div><div><span>Industry</span>Internet</div></div></div><div class="act offer-btn">Make Offer</div></div>
    <div class="item" style="height:110px"><div><h4>domainry.example</h4><div class="specs"><div><span>Type</span>Domain</div><div><span>Domain Age</span>20 years</div><div><span>Industry</span>Internet</div></div></div><div class="act offer-btn">Make Offer</div></div>
    <div class="item" style="height:111px"><div><h4>Parksourcehub.example</h4><div class="specs"><div><span>Type</span>Domain</div><div><span>Domain Age</span>20 years</div><div><span>Industry</span>Internet</div></div></div><div class="act view">View Listing</div></div>
    <div class="item" style="height:99px"><div><h4>loremipsum.example</h4><div class="specs"><div><span>Type</span>Domain</div><div><span>Domain Age</span>20 years</div><div><span>Industry</span>Internet</div></div></div><div class="act offer-btn">Make Offer</div></div>
  </div>

  <nav class="pager" style="top:1430px"><span class="arr">‹</span><span class="on">1</span><span>2</span><span>3</span><span>4</span><span>5 ...... 130</span><span class="arr">›</span></nav>

  <div class="help" style="top:1492px;height:200px">
    <h2 class="center section-h" style="top:53px">Questions?We're happy to help</h2>
    <div class="contact" style="left:297px;top:101px"><span class="ico"><svg width="20" height="20" viewBox="0 0 24 24"><path d="M6.6 10.8a15 15 0 0 0 6.6 6.6l2.2-2.2c.3-.3.7-.4 1-.2 1.1.4 2.3.6 3.6.6.6 0 1 .4 1 1V20c0 .6-.4 1-1 1A17 17 0 0 1 3 4c0-.6.4-1 1-1h3.5c.6 0 1 .4 1 1 0 1.3.2 2.5.6 3.6.1.3 0 .7-.2 1z" fill="#1a5cf0"/></svg></span>+1 - 123-456-7890</div>
    <div class="contact" style="left:525px;top:101px"><span class="ico"><svg width="20" height="16" viewBox="0 0 20 16"><rect x="1" y="1" width="18" height="14" rx="1" fill="#1a5cf0"/><path d="m1 2 9 7 9-7" stroke="#fff" stroke-width="1.6" fill="none"/></svg></span>Write Us</div>
  </div>
  <footer class="footer" style="top:1692px;height:54px"><span>Terms &amp; Conditions</span><span>I</span><span>Contact Us</span><span>I</span><span>Copyright© 2023.All Right Reserved</span></footer>
</section>

</body>
</html>
```